New Business Card for Web Design/Internet Marketing Company

Looking for a great looking new business card. We are a 10 year old web design, internet marketing and website management company that works mostly with small businesses.

Our new card needs to better match the colors and style of our website, be bold, extremely usable and slightly edgy.

Target Market(s)

Small/Medium businesses that have websites

Industry/Entity Type

Internet

Requirements
Must have
• Front and back design, full color, rounded corners please

Must use the colors/style of our website (JPG provided)

INFO FOR CARDS (as readable as possible please)
Mark Pellow
President/CEO
mark@brightlanesites.com
Phone: 520-481-7093
Toll Free: 866-481-7093
Address: 4315 E. Kestrel Ave. Ste. 140, Tucson, AZ 85733

THINGS I WANT TO PROMOTE (if there is room):
1. Our Website - www.brightlanesites.com

2. Social Media
Twitter: @brightlanesites
Facebook: social.brightlanesites.com

3. Our Services
Web Design
Internet Marketing
Website Management

```html
<!DOCTYPE html>
<html lang="en">
<head>
<meta charset="utf-8">
<title>Bright Lane Sites – Business Card</title>
<link rel="stylesheet" href="https://fonts.googleapis.com/css2?family=Yanone+Kaffeesatz:wght@400;600;700&display=swap">
<style>
  :root {
    --page: #f1f1f6;
    --card: #c9c9cb;
    --card-light: #dcdcde;
    --orange: #ee9a3f;
    --yellow: #f4bf4a;
    --charcoal: #3b3b3d;
    --blue: #1f8fc7;
    --blue-dark: #156c9a;
    --brown: #8a6a4a;
    --ink: #333336;
    --white: #ffffff;
  }
  * { box-sizing: border-box; margin: 0; padding: 0; }
  html, body { width: 1200px; height: 900px; overflow: hidden; }
  body {
    background: var(--page);
    font-family: "Yanone Kaffeesatz", "Arial Narrow", sans-serif;
    color: var(--ink);
    position: relative;
  }
  .card {
    position: absolute;
    left: 320px;
    width: 560px;
    height: 320px;
    border-radius: 22px;
    overflow: hidden;
    background: var(--card);
    box-shadow: 0 10px 30px rgba(0,0,0,0.15);
  }
  .card--front { top: 100px; }
  .card--back { top: 480px; background: var(--card-light); }
  .card__waves { position: absolute; inset: 0; width: 100%; height: 100%; }
  .brand {
    position: absolute;
    display: flex;
    align-items: center;
    gap: 8px;
  }
  .brand__dot {
    width: 24px; height: 24px; border-radius: 50%;
    background: var(--orange);
    flex: none;
  }
  .brand__name {
    font-weight: 700;
    font-size: 30px;
    color: var(--blue);
    line-height: 1;
    white-space: nowrap;
  }
  .brand__tagline {
    position: absolute;
    font-size: 13px;
    color: var(--ink);
  }
  .card--front .brand { left: 32px; top: 98px; }
  .card--front .brand__tagline { left: 64px; top: 130px; }
  .person { position: absolute; left: 34px; top: 158px; }
  .person__name { font-size: 32px; font-weight: 400; color: var(--brown); line-height: 1; }
  .person__title { font-size: 14px; color: var(--ink); margin-top: 2px; }
  .contacts {
    position: absolute; left: 250px; top: 94px;
    list-style: none;
    display: flex; flex-direction: column; gap: 8px;
  }
  .contact { display: flex; align-items: center; gap: 8px; font-size: 16px; white-space: nowrap; }
  .contact__icon {
    width: 16px; height: 16px; border-radius: 50%;
    background: var(--blue-dark);
    display: flex; align-items: center; justify-content: center; flex: none;
  }
  .contact__icon svg { width: 10px; height: 10px; fill: var(--white); }
  .contact--tollfree {
    background: var(--blue);
    color: var(--white);
    font-weight: 600;
    font-size: 20px;
    padding: 3px 14px 3px 4px;
    border-radius: 16px;
    align-self: flex-start;
  }
  .contact--tollfree .contact__icon { background: var(--white); }
  .contact--tollfree .contact__icon svg { fill: var(--blue); }
  .card--back .brand { left: 0; right: 0; top: 104px; justify-content: center; }
  .card--back .brand__tagline { left: 0; right: 0; top: 136px; text-align: center; }
  .services {
    position: absolute; left: 80px; right: 80px; top: 162px;
    background: var(--blue);
    color: var(--white);
    border-radius: 18px;
    text-align: center;
    font-weight: 600;
    font-size: 19px;
    padding: 5px 0;
    letter-spacing: 0.3px;
  }
  .social {
    position: absolute; left: 0; right: 0; top: 204px;
    display: flex; justify-content: center; gap: 24px;
    list-style: none;
  }
  .social .contact { font-size: 16px; }
</style>
</head>
<body>

<section class="card card--front" aria-label="Business card front">
  <svg class="card__waves" viewBox="0 0 560 320" preserveAspectRatio="none" aria-hidden="true">
    <path d="M0 0 H560 V40 C470 30 430 70 360 60 C280 48 200 10 120 40 C70 58 30 60 0 58 Z" fill="var(--orange)"/>
    <path d="M0 262 C30 266 60 268 110 256 C190 236 250 254 340 272 C430 290 480 250 560 258 V320 H0 Z" fill="var(--yellow)"/>
    <path d="M0 290 C80 280 150 270 240 290 C330 310 420 300 560 282 V320 H0 Z" fill="var(--orange)"/>
  </svg>

  <div class="brand"><span class="brand__dot"></span><span class="brand__name">Bright Lane Sites</span></div>
  <p class="brand__tagline">web design studio</p>

  <div class="person">
    <p class="person__name">Mark Pellow</p>
    <p class="person__title">President/CEO</p>
  </div>

  <ul class="contacts">
    <li class="contact"><span class="contact__icon"><svg viewBox="0 0 10 10"><path d="M5 0a3.5 3.5 0 0 0-3.5 3.5C1.5 6 5 10 5 10s3.5-4 3.5-6.5A3.5 3.5 0 0 0 5 0zm0 5a1.5 1.5 0 1 1 0-3 1.5 1.5 0 0 1 0 3z"/></svg></span>4315 E. Kestrel Ave. Ste. 140, Tucson, AZ 85733</li>
    <li class="contact"><span class="contact__icon"><svg viewBox="0 0 10 10"><path d="M2 0l2 2.5-1 1.2c.6 1.3 1.6 2.3 2.9 2.9l1.2-1L10 8l-1.3 1.6C4.5 9.6.4 5.5.4 1.3z"/></svg></span>520-481-7093</li>
    <li class="contact contact--tollfree"><span class="contact__icon"><svg viewBox="0 0 10 10"><path d="M2 0l2 2.5-1 1.2c.6 1.3 1.6 2.3 2.9 2.9l1.2-1L10 8l-1.3 1.6C4.5 9.6.4 5.5.4 1.3z"/></svg></span>866-481-7093 (Toll Free)</li>
    <li class="contact"><span class="contact__icon"><svg viewBox="0 0 10 10"><path d="M0 2h10v6H0zM0 2l5 3.5L10 2" stroke="#fff" stroke-width="0.6" fill="none"/></svg></span>mark@brightlanesites.com</li>
    <li class="contact"><span class="contact__icon"><svg viewBox="0 0 10 10"><circle cx="5" cy="5" r="4.2" stroke="#fff" stroke-width="1" fill="none"/><path d="M1 5h8M5 1v8" stroke="#fff" stroke-width="0.8"/></svg></span>www.brightlanesites.com</li>
  </ul>
</section>

<section class="card card--back" aria-label="Business card back">
  <svg class="card__waves" viewBox="0 0 560 320" preserveAspectRatio="none" aria-hidden="true">
    <path d="M300 0 H560 V70 C500 60 440 30 380 20 C350 14 320 8 300 0 Z" fill="var(--orange)"/>
    <path d="M0 20 C120 10 220 50 340 70 C440 86 500 70 560 96 V126 C500 104 430 118 330 100 C210 80 110 46 0 50 Z" fill="var(--charcoal)"/>
    <path d="M0 240 C90 230 180 256 290 246 C400 236 470 220 560 236 V262 C470 250 400 266 290 274 C180 282 90 258 0 268 Z" fill="var(--charcoal)"/>
    <path d="M0 268 C90 258 180 282 290 274 C360 270 400 290 420 320 H0 Z" fill="var(--orange)"/>
  </svg>

  <div class="brand"><span class="brand__dot"></span><span class="brand__name">Bright Lane Sites</span></div>
  <p class="brand__tagline">web design studio</p>

  <p class="services">Web Design | Internet Marketing | Website Management</p>

  <ul class="social">
    <li class="contact"><span class="contact__icon"><svg viewBox="0 0 10 10"><circle cx="5" cy="5" r="2.5"/></svg></span>social.brightlanesites.com</li>
    <li class="contact"><span class="contact__icon"><svg viewBox="0 0 10 10"><circle cx="5" cy="5" r="2.5"/></svg></span>@brightlanesites</li>
  </ul>
</section>

</body>
</html>
```